Landing page for a cyber security service provider called 'Lumen Grove'

The client is a new cyber security company in need of a website landing page at lumengrove.example.

Their visual identity is modern, playful, clean and uncluttered and represents innovation, connectivity and approachability.

The company logo is provided in black (attached) but the client is open to changing the colour to align with the new website design.

The landing page needs to contain:
- A call to action with a 'Get Started' button
-Links to blank 'How it works', 'Products', 'Pricing', 'About Us' and 'Contact Us' pages (that we'll fill out later)

Target Market(s)

Medium to large businesses who probably don't understand cyber / cyber security but need their business to be protected.

Industry/Entity Type

Cyber Security

Coding

Coded - Design and coding required

Number of Pages Required

1 page

Font styles to use
Sans Serif
Other font styles liked:
• Helvetica

Requirements
Nice to have
• Hero banner at the top of the landing page.
Should not have
• Should not look like a traditional cyber / cyber security design (eg no dark blue/ black, red/black colour combinations). Please no military styles (eg no shields, cannons, swords, guns)

```html
<!DOCTYPE html>
<html lang="en">
<head>
<meta charset="utf-8">
<title>Lumen Grove — Empower Your Cybersecurity</title>
<link href="https://fonts.googleapis.com/css2?family=Hind:wght@400;500;600&family=Montserrat:wght@400;500;600&display=swap" rel="stylesheet">
<style>
:root{
  --green:#16775a;
  --green-deep:#1c5e4b;
  --green-mid:#2b6f5b;
  --green-soft:#3c8a73;
  --ink:#1c1f1e;
  --grey:#8a8f8c;
  --line:#e3e5e3;
  --mist:#f0f1ef;
  --white:#ffffff;
  --head:"Hind",Helvetica,Arial,sans-serif;
  --body:"Montserrat",Helvetica,Arial,sans-serif;
}
*{margin:0;padding:0;box-sizing:border-box}
html,body{width:1200px;height:4165px;overflow:hidden}
body{position:relative;font-family:var(--body);color:var(--ink);background:var(--white)}
.abs{position:absolute}
h1,h2,h3{font-family:var(--head);font-weight:500}
.rule{position:absolute;height:2px;width:53px;background:#cfd3d0}
.rule.light{background:var(--white)}
.btn{position:absolute;display:flex;align-items:center;justify-content:center;border-radius:30px;font-size:11.5px;font-weight:600;letter-spacing:.3px;text-transform:uppercase;color:var(--white);text-decoration:none;white-space:nowrap}
.btn.solid{background:var(--green)}
.btn.ghost{border:1.5px solid var(--white)}

/* hero */
.hero{position:absolute;left:0;top:0;width:1200px;height:555px;background:radial-gradient(circle at 560px 250px,#3f8f78 0,#2b7561 35%,#226552 70%,#1d5a49 100%)}
.hero-shade{position:absolute;inset:0;background:linear-gradient(90deg,rgba(20,70,56,.35),rgba(20,70,56,0) 60%,rgba(20,70,56,.25))}
.brand{position:absolute;left:125px;top:62px;display:flex;align-items:center;gap:10px;color:var(--white);font-family:var(--head);font-size:28px;font-weight:500}
.brand-dot{width:16px;height:16px;border-radius:50%;background:var(--white)}
.nav{position:absolute;top:68px;left:0;font-size:12px;font-weight:500}
.nav a{position:absolute;color:var(--white);text-decoration:none;white-space:nowrap}
.hero h1{position:absolute;left:0;width:1200px;top:168px;text-align:center;color:var(--white);font-size:58px;line-height:61px;font-weight:500}
.hero p{position:absolute;left:0;width:1200px;top:308px;text-align:center;color:var(--white);font-size:12.5px}

/* story */
.sec-title{position:absolute;left:100px;font-size:34px;color:var(--ink)}
.story-lead{position:absolute;left:537px;top:636px;width:530px;font-family:var(--head);font-size:23px;line-height:29px;color:var(--ink)}
.story-note{position:absolute;left:537px;top:738px;width:560px;font-size:12px;line-height:21px;color:var(--grey)}
.divider{position:absolute;left:100px;width:1000px;height:1px;background:var(--line)}

/* services */
.band{position:absolute;left:0;top:1342px;width:1200px;height:560px;background:var(--green)}
.card{position:absolute;width:327px;height:374px;color:var(--white)}
.card .photo{position:absolute;inset:0}
.card h3{position:absolute;left:40px;top:40px;font-size:23px;font-weight:500}
.card .more{position:absolute;left:40px;bottom:42px;font-size:11.5px;font-weight:500;text-transform:uppercase;letter-spacing:.3px}
.cta h2{position:absolute;left:0;width:1200px;text-align:center;color:var(--white);font-size:36px}
.cta p{position:absolute;left:0;width:1200px;text-align:center;color:var(--white);font-size:12.5px;line-height:21px}

/* work */
.work{position:absolute;left:0;top:1902px;width:1200px;height:485px;background:linear-gradient(100deg,#2f6d5c 0,#285f50 45%,#337563 70%,#265a4c 100%)}
.work h2{position:absolute;left:100px;top:84px;font-size:34px;color:var(--white)}
.work p{position:absolute;left:100px;top:166px;width:450px;font-size:12.5px;line-height:21px;color:var(--white)}
.stat{position:absolute;width:224px;height:155px;background:var(--white);text-align:center}
.stat b{display:block;margin-top:40px;font-family:var(--head);font-weight:500;font-size:37px;line-height:40px;color:var(--ink)}
.stat span{display:block;margin-top:12px;font-size:11.5px;color:var(--grey)}

/* why */
.why-title{position:absolute;left:0;width:1200px;top:2466px;text-align:center;font-size:34px}
.mist{position:absolute;left:0;top:3047px;width:1200px;height:703px;background:var(--mist)}
.reason{position:absolute;left:663px;width:377px}
.reason .num{position:absolute;left:5px;top:0;font-family:var(--head);font-size:22px;color:var(--green)}
.reason h3{position:absolute;left:45px;top:0;font-size:18px;font-weight:500;color:var(--ink)}
.reason p{position:absolute;left:45px;top:32px;width:335px;font-size:12px;line-height:21px;color:var(--grey)}
.reason-line{position:absolute;left:663px;width:377px;height:1px;background:#d9dcda}

/* testimonials */
.quote-mark{position:absolute;font-family:Georgia,serif;font-weight:700;color:var(--green);line-height:1}
.quote{position:absolute;left:100px;width:400px;font-size:14px;line-height:20px;color:var(--ink);font-weight:500}
.author{position:absolute;left:100px;font-size:12px;color:var(--grey)}
.feature{position:absolute;left:619px;top:3285px;width:481px;height:365px;background:var(--green);color:var(--white)}
.feature p{position:absolute;left:40px;top:112px;width:400px;font-family:var(--head);font-size:23px;line-height:28px;font-weight:500}
.feature small{position:absolute;left:40px;top:294px;font-size:12px}

/* footer */
.closing{position:absolute;left:0;top:3750px;width:1200px;height:415px;background:var(--green-deep)}
.closing h2{position:absolute;left:0;width:1200px;top:102px;text-align:center;font-size:36px;color:var(--white)}
.closing p{position:absolute;left:0;width:1200px;top:168px;text-align:center;font-size:12.5px;line-height:21px;color:var(--white)}
.closing .btn.solid{background:var(--green-soft)}
.closing .base{position:absolute;left:0;top:360px;width:1200px;height:1px;background:#5f9384}
.closing .copy{position:absolute;left:0;width:1200px;top:390px;text-align:center;font-size:11.5px;color:var(--white)}
</style>
</head>
<body>

<header class="hero">
  <div class="abs" style="inset:0" role="img" aria-label="Close-up of a glowing teal security dashboard screen with data readouts"></div>
  <div class="hero-shade"></div>
  <div class="brand"><span class="brand-dot"></span>Lumen Grove</div>
  <nav class="nav">
    <a href="#" style="left:500px">How it works</a>
    <a href="#" style="left:604px">Products</a>
    <a href="#" style="left:686px">Pricing</a>
    <a href="#" style="left:758px">About Us</a>
    <a href="#" style="left:842px">Contact Us</a>
  </nav>
  <a href="#" class="btn ghost" style="left:944px;top:55px;width:156px;height:42px">Get Started</a>
  <h1>Empower Your<br>Cybersecurity</h1>
  <p>Seamless protection for your business with innovative solutions and user-friendly design.</p>
  <a href="#" class="btn solid" style="left:524px;top:356px;width:152px;height:40px;background:var(--green-deep)">Get Started</a>
</header>

<section class="story">
  <h2 class="sec-title" style="top:636px">Our Story</h2>
  <div class="rule" style="left:100px;top:705px"></div>
  <p class="story-lead">LumenGrove offers cutting-edge cybersecurity solutions tailored for medium to large businesses.</p>
  <p class="story-note">At LumenGrove, we prioritize trust and connectivity, providing essential services without the need for technical knowledge.</p>
  <div class="divider" style="top:844px"></div>
</section>

<section class="services">
  <div class="band"></div>
  <h2 class="sec-title" style="top:910px">Our Services</h2>
  <div class="rule" style="left:100px;top:978px"></div>

  <article class="card" style="left:100px;top:1030px">
    <div class="photo" role="img" aria-label="Screen showing the word security with a pixel cursor" style="background:linear-gradient(160deg,#2f6a5a,#245546 60%,#357565)"></div>
    <h3>Threat Monitoring</h3><span class="more">Read More</span>
  </article>
  <article class="card" style="left:437px;top:1113px">
    <div class="photo" role="img" aria-label="Silhouette in shadow against glowing code" style="background:linear-gradient(160deg,#316a5b,#285a4c 50%,#3a7666)"></div>
    <h3>Incident Response</h3><span class="more">Read More</span>
  </article>
  <article class="card" style="left:773px;top:1030px">
    <div class="photo" role="img" aria-label="Green source code on a monitor" style="background:linear-gradient(150deg,#367a67,#2a6251 60%,#418673)"></div>
    <h3>Security Audits</h3><span class="more">Read More</span>
  </article>

  <div class="cta">
    <div class="rule light" style="left:573px;top:1612px"></div>
    <h2 style="top:1634px">Enhance Your Security Today</h2>
    <p style="top:1690px">Protect your business with our top-notch cybersecurity services. Join us in ensuring your<br>digital safety.</p>
    <a href="#" class="btn ghost" style="left:534px;top:1761px;width:152px;height:39px">Get Started</a>
  </div>
</section>

<section class="work" role="img" aria-label="Soft photo of people reviewing work on screens">
  <h2>Our Work</h2>
  <div class="rule light" style="left:100px;top:145px"></div>
  <p>Explore our portfolio showcasing successful cybersecurity solutions for businesses like yours.</p>
  <div class="stat" style="left:642px;top:84px"><b>93%</b><span>Short Description</span></div>
  <div class="stat" style="left:876px;top:84px"><b>175+</b><span>Short Description</span></div>
  <div class="stat" style="left:642px;top:248px"><b>30K</b><span>Short Description</span></div>
  <div class="stat" style="left:876px;top:248px"><b>1.5Mil</b><span>Short Description</span></div>
</section>

<div class="mist"></div>

<section class="why">
  <h2 class="why-title">Why Choose Us</h2>
  <div class="rule" style="left:573px;top:2539px"></div>
  <div class="abs" role="img" aria-label="Person at a laptop with a teal VPN app on screen" style="left:100px;top:2589px;width:495px;height:477px;background:linear-gradient(140deg,#e9ece9 0,#cfd6d3 40%,#3fa6a6 55%,#d8dcd9 80%,#efe9e2 100%)"></div>

  <div class="reason" style="top:2625px"><span class="num">1</span><h3>Innovative Solutions</h3><p>Experience cutting-edge cybersecurity solutions and protect your business with ease.</p></div>
  <div class="reason-line" style="top:2715px"></div>
  <div class="reason" style="top:2733px"><span class="num">2</span><h3>User-Friendly Design</h3><p>Minimalistic design and user-friendly navigation for a seamless cybersecurity experience.</p></div>
  <div class="reason-line" style="top:2824px"></div>
  <div class="reason" style="top:2841px"><span class="num">3</span><h3>Trust &amp; Connectivity</h3><p>Emphasis on trust and connectivity ensures essential services for robust cybersecurity without technical hassle.</p></div>
</section>

<section class="testimonials">
  <h2 class="sec-title" style="top:3164px">Testimonials</h2>
  <div class="rule" style="left:100px;top:3235px"></div>

  <span class="quote-mark" style="left:100px;top:3308px;font-size:34px">”</span>
  <p class="quote" style="top:3350px">LumenGrove has transformed our cybersecurity approach. Their solutions are top-notch and user-friendly, making security a breeze.</p>
  <span class="author" style="top:3436px">Dario Fenwick</span>
  <div class="abs" style="left:100px;top:3480px;width:435px;height:1px;background:#d9dcda"></div>
  <span class="quote-mark" style="left:100px;top:3504px;font-size:34px">”</span>
  <p class="quote" style="top:3546px">Impressed by LumenGrove’s professionalism and innovation in cybersecurity solutions. They deliver exactly what they promise.</p>
  <span class="author" style="top:3632px">Owen Castell</span>

  <div class="feature">
    <span class="quote-mark" style="left:40px;top:26px;font-size:70px;color:var(--white)">”</span>
    <p>LumenGrove exceeded my expectations with their services. I feel confident in the security they provide for our business.</p>
    <small>Nadia Brooks</small>
  </div>
</section>

<footer class="closing">
  <div class="rule light" style="left:573px;top:83px"></div>
  <h2>Secure Your Business Today</h2>
  <p>Take the first step towards robust cybersecurity for your business.<br>Contact us to get started.</p>
  <a href="#" class="btn solid" style="left:524px;top:235px;width:152px;height:40px">Get Started</a>
  <div class="base"></div>
  <div class="copy">Copyright © 2024</div>
</footer>

</body>
</html>
```